Brimovex business card

Based on company logo and website given , to design a business card temple. Slogan "Your furry friends deserves the best"
Color style please refer to our website

```html
<!DOCTYPE html>
<html lang="en">
<head>
<meta charset="UTF-8">
<title>Brimovex Business Card</title>
<link href="https://fonts.googleapis.com/css2?family=Montserrat:wght@400;500;600&display=swap" rel="stylesheet">
<style>
  :root {
    --brand-blue: #0b67bc;
    --text-grey: #6d6e71;
    --paper: #ffffff;
    --backdrop: #bdbdbd;
  }
  * { margin: 0; padding: 0; box-sizing: border-box; }
  html, body {
    width: 1200px; height: 1200px; overflow: hidden;
    background: var(--backdrop);
    font-family: "Montserrat", Arial, sans-serif;
  }
  .canvas { position: relative; width: 1200px; height: 1200px; }
  .card {
    position: absolute; left: 230px; width: 741px; height: 423px;
  }
  .card--front { top: 140px; background: var(--paper); }
  .card--back { top: 638px; background: var(--brand-blue); }

  .wordmark {
    position: absolute; transform: translate(-50%, -50%);
    font-weight: 600; letter-spacing: 1px; white-space: nowrap; line-height: 1;
  }
  .card--front .wordmark { left: 215px; top: 233px; font-size: 58px; color: var(--brand-blue); }
  .card--back .wordmark { left: 370px; top: 232px; font-size: 88px; color: var(--paper); }

  .divider {
    position: absolute; left: 411px; top: 109px; width: 1.5px; height: 211px;
    background: var(--brand-blue);
  }
  .contact { position: absolute; left: 460px; top: 104px; color: var(--text-grey); }
  .contact__name {
    font-size: 25px; font-weight: 500; color: var(--brand-blue);
    letter-spacing: 0.8px; line-height: 30px;
  }
  .contact__role { font-size: 18px; line-height: 22px; margin-top: 2px; }
  .contact__address { font-size: 18px; line-height: 24px; margin-top: 12px; letter-spacing: 0.3px; }
  .contact__list { list-style: none; margin-top: 10px; }
  .contact__item {
    display: flex; align-items: center; font-size: 18px; line-height: 24.8px; letter-spacing: 0.3px;
  }
  .contact__icon { width: 14px; height: 14px; margin-right: 7px; margin-left: -1px; flex: none; }

  .tagline {
    position: absolute; left: 0; width: 100%; top: 376px; text-align: center;
    color: var(--paper); font-size: 17.5px; letter-spacing: 0.8px;
  }
</style>
</head>
<body>
<div class="canvas">
  <section class="card card--front">
    <div class="wordmark">Brimovex</div>
    <div class="divider"></div>
    <div class="contact">
      <div class="contact__name">DANIEL HARPER</div>
      <div class="contact__role">Director</div>
      <div class="contact__address">418 W. Larkspur Ave #210<br>Fairhaven, NV 89120</div>
      <ul class="contact__list">
        <li class="contact__item">
          <svg class="contact__icon" viewBox="0 0 16 16" fill="none" stroke="#0b67bc" stroke-width="1.8" stroke-linecap="round"><path d="M4 2 L6 5 L5 7 Q6.5 10 9 11.5 L11 10.5 L14 12.5 L12.5 14.5 Q6 14 2 5 Z"/></svg>
          555.214.0187
        </li>
        <li class="contact__item">
          <svg class="contact__icon" viewBox="0 0 16 16" fill="#0b67bc"><rect x="4" y="1.5" width="8" height="4"/><rect x="1" y="5.5" width="14" height="6" rx="1"/><rect x="4" y="10" width="8" height="4.5" fill="#fff" stroke="#0b67bc" stroke-width="1.4"/></svg>
          555-214-0189
        </li>
        <li class="contact__item">
          <svg class="contact__icon" viewBox="0 0 16 16" fill="none" stroke="#0b67bc" stroke-width="1.6"><rect x="1.5" y="3.5" width="13" height="9"/><path d="M1.5 3.5 L8 9 L14.5 3.5"/></svg>
          info@Brimovex.com
        </li>
        <li class="contact__item">
          <svg class="contact__icon" viewBox="0 0 16 16" fill="none" stroke="#0b67bc" stroke-width="1.2"><circle cx="8" cy="8" r="6.5"/><ellipse cx="8" cy="8" rx="3" ry="6.5"/><path d="M1.5 8 H14.5 M2.5 5 H13.5 M2.5 11 H13.5"/></svg>
          www.Brimovex.com
        </li>
      </ul>
    </div>
  </section>

  <section class="card card--back">
    <div class="wordmark">Brimovex</div>
    <p class="tagline">YOUR FURRY FRIENDS DESERVES THE BEST</p>
  </section>
</div>
</body>
</html>
```